Front label design for health food product

I need a front label designed for a new health food product I am introducing for my health food business - Dr Vitagrove. The product is Acai Berry Powder (NAFB certified organic).

Label Dimensions: Approx. 140mm high x 130mm wide.

The weight to be placed on the label is: 200g Net

The Acai Berry Powder is a native berry grown in South America and is dark purple in colour, high in antioxidants, nutrients, etc. Images of Acai berries are readily available on the web (eg. pixmarlo.com).

The powder can be used to make smoothies, shakes, sprinkle on breakfast cereal, deserts, etc for an antioxidant boost.

I would like a simple, yet classy design incorporating purple colours, an image of the fruit and acai palm tree, my Dr Vitagrov logo (attached file), and possibly an image of where they are grown in the background as a watermark?? (eg, map of South America with.

Designs of existing labels can be seen on the www.drvitagrove.com.au website. However, I don't necessarily want to have the same format as these, maybe the same top part only to keep some customer .

Below is the Wikipedia pages for the Acai Berry for more information.

http://en.knowpedia-example.org/wiki/Acai_Berry#Fruit
Updates

Sorry I forgot to include the dimensions for the label. The dimensions will be 140mm high x 130mm wide.

Also the weight on the label needs to be 150g Net on the bottom, centre of the front label.

Industry/Entity Type

Health

Requirements
Must have
• Dr VitaGrove Logo
Image of Acai Berries
Health food 'feel'
Image of NAFB organic logo

```html
<!DOCTYPE html>
<html lang="en">
<head>
<meta charset="utf-8">
<title>Acai Berry Powder – Front Label</title>
<link rel="stylesheet" href="https://fonts.googleapis.com/css2?family=Source+Sans+3:wght@400;600;700&family=Arimo:wght@400&display=swap">
<style>
  :root {
    --purple-deep: #4a2478;
    --purple-mid: #6a3597;
    --purple-frame: #7a2e8e;
    --red-flag: #e41e26;
    --white: #ffffff;
    --ink: #111111;
    --paper: #ffffff;
    --crop: #9a9a9a;
    --leaf-green: #5d8a4a;
  }
  * { margin: 0; padding: 0; box-sizing: border-box; }
  html, body { width: 1134px; height: 1200px; overflow: hidden; background: var(--paper); }
  .sheet { position: relative; width: 1134px; height: 1200px; font-family: "Source Sans 3", "Myriad Pro", sans-serif; }

  .crop-marks { position: absolute; inset: 0; }

  .label {
    position: absolute; left: 100px; top: 100px; width: 937px; height: 979px;
    overflow: hidden;
    background: linear-gradient(180deg, var(--purple-deep) 0%, var(--purple-mid) 30%, #8a62ad 44%, #d9cde4 56%, #f5f3f6 64%, #ffffff 100%);
  }
  .label-frame {
    position: absolute; left: 35px; top: 66px; width: 866px; height: 878px;
    border: 4px solid var(--purple-frame);
  }

  .claim-corner { position: absolute; left: 0; top: 0; width: 303px; height: 291px; }
  .claim-list {
    position: absolute; left: -20px; top: 88px; width: 300px;
    transform: rotate(-45deg); transform-origin: center;
    list-style: none; color: var(--white); font-weight: 700; font-size: 17px;
    line-height: 22px; text-align: center;
  }
  .claim-list li::before { content: "\2713\00a0"; }

  .brand-tab {
    position: absolute; left: 386px; top: 0; width: 166px; height: 226px;
    background: var(--white);
    box-shadow: 0 3px 8px rgba(0,0,0,0.25);
    display: flex; flex-direction: column; align-items: center; justify-content: flex-end;
    padding-bottom: 34px; gap: 14px;
  }
  .brand-dot { width: 40px; height: 40px; border: 3px solid var(--purple-frame); }
  .brand-name { color: var(--purple-frame); font-weight: 600; font-size: 20px; }

  .cert-badge {
    position: absolute; left: 768px; top: 251px; width: 108px; height: 108px;
    border-radius: 50%; background: var(--white);
    border: 6px solid var(--leaf-green);
  }

  .product-title {
    position: absolute; left: 0; width: 100%; top: 330px;
    text-align: center; color: var(--white); font-weight: 400;
    font-size: 122px; line-height: 1;
  }
  .product-type {
    position: absolute; left: 0; width: 100%; top: 488px;
    text-align: center; color: var(--white); font-weight: 400;
    font-size: 38px; letter-spacing: 30px; padding-left: 30px;
  }

  .berry-photo {
    position: absolute; left: 90px; top: 545px; width: 760px; height: 360px;
    background: radial-gradient(ellipse 55% 45% at 50% 45%, rgba(42,26,46,0.85) 0%, rgba(60,40,70,0.55) 45%, rgba(120,150,100,0.25) 75%, rgba(255,255,255,0) 100%);
  }

  .net-weight {
    position: absolute; left: 0; width: 100%; top: 880px;
    text-align: center; color: var(--ink); font-weight: 700; font-size: 30px;
  }

  .proof-caption {
    position: absolute; left: 178px; top: 1088px;
    font-family: "Arimo", Arial, sans-serif; font-size: 36px; color: var(--ink);
    word-spacing: 4px;
  }
  .proof-caption .gap { display: inline-block; width: 80px; }
</style>
</head>
<body>
<div class="sheet">
  <svg class="crop-marks" width="1134" height="1200" viewBox="0 0 1134 1200" aria-hidden="true">
    <g stroke="var(--crop)" stroke-width="2">
      <line x1="100" y1="0" x2="100" y2="70"/>
      <line x1="1037" y1="0" x2="1037" y2="70"/>
      <line x1="0" y1="100" x2="70" y2="100"/>
      <line x1="1064" y1="100" x2="1134" y2="100"/>
      <line x1="0" y1="1079" x2="70" y2="1079"/>
      <line x1="1064" y1="1079" x2="1134" y2="1079"/>
      <line x1="100" y1="1130" x2="100" y2="1200"/>
      <line x1="1037" y1="1130" x2="1037" y2="1200"/>
    </g>
  </svg>

  <section class="label">
    <div class="berry-photo" role="img" aria-label="Photograph of dark purple acai berries with green leaves on a white surface"></div>
    <div class="label-frame"></div>

    <svg class="claim-corner" viewBox="0 0 303 291" aria-hidden="true">
      <polygon points="0,0 303,0 0,291" fill="var(--red-flag)"/>
    </svg>
    <ul class="claim-list">
      <li>100% Natural</li>
      <li>Certified Organic</li>
      <li>High In Antioxidants</li>
    </ul>

    <div class="brand-tab">
      <span class="brand-dot"></span>
      <span class="brand-name">Dr Vitagrove</span>
    </div>

    <div class="cert-badge" role="img" aria-label="Organic certification badge"></div>

    <h1 class="product-title">Acai Berry</h1>
    <p class="product-type">POWDER</p>

    <p class="net-weight">150g Net</p>
  </section>

  <p class="proof-caption">Option 5<span class="gap"></span>size H=140mm x W=130mm</p>
</div>
</body>
</html>
```